energy rating company

Web Design graphics and layout only

To create two pages for the website. First the home page and the second is the design for the job board for our clients use after login. I have attached files that explain in detail what the pages should have and the purpose/desires of each object. Please read these thoroughly.

The webpages need to be clean, professional, easy on the eye, obvious in all its buttons and functions with a strong call to action on the home page and branding and clean, great and obvious looking buttons and very simple but dynamic as well. We wish to be seen as contemporary.

Business Concept

Our business concept is simple, to build a website whereby our clients will be able to upload jobs for energy raters to quote on and subsequent complete the work if their quote is selected. To link energy ratings that are required with energy raters via our website. Similarly to the varlo website, jobs will be “advertised” on the job board and raters will select which jobs they wish to quote for.

I have attached a Word document explaining all the parts of the website and another word document showing what we are sort of after and a excel spreadsheet as well. Please read these in conjunction with this brief!
Updates

Dear All

I have submitted with my brief a word doc and excel spreadsheet of the two pages I want created.  However this is not the layout or design I want, I only put it together so that you will need to know what is required on each page.  Feel free to change and redesign it all.

Also the second page does not require the "process" logo or any other menu items except the first five being Home, How it works, About Us, testimonials and Contact us as per the home page.

We also are looking for something very professional and very clean.  It should be very easy to see exactly what you are looking for.

I will also extend the deadline for new designers!!  I am excited to see your talents!!

Thanks

I have increase budget and posted a note saying feel free to change all the details layout etc on my brief just include everything!!! 

Wanting a professional corporate look...

Want a professional corporate look

We have changed our minds and you we no longer require the process to be on the home page.

Thanks

Target Market(s)

Target Market

Home Inspection Companies
Pest Inspection Companies
Residential home buyers/sellers
Real Estate companies

Industry/Entity Type

It Company

Number of Pages Required

1 page

Requirements
Must have
• Colours and Styles

• The website should be mainly white as I believe it is seen as clean and simple with colour from the logos, but can be swayed if it projects the image we are after.

• It should be obvious and process orientated and I do believe symbols, pictures, etc should replace words where possible.

```html
<!DOCTYPE html>
<html lang="en">
<head>
<meta charset="utf-8">
<title>Verdio Australia – Web Pages</title>
<link href="https://fonts.googleapis.com/css2?family=Roboto:wght@300;400;500;700&family=Oswald:wght@300;600&display=swap" rel="stylesheet">
<style>
:root{
  --bg-green:#21944a;
  --green:#2a9a45;
  --green-light:#8cc63f;
  --rust:#b5521b;
  --rust-dark:#9c4315;
  --ochre:#c08a2a;
  --gold:#e0a823;
  --yellow:#f7ec13;
  --row-a:#c5e3b5;
  --row-b:#e0f0d6;
  --blue:#4a9bd6;
  --text:#555;
  --white:#fff;
}
*{box-sizing:border-box;margin:0;padding:0}
html,body{width:770px;height:1200px;overflow:hidden}
body{position:relative;background:var(--white);font-family:"Roboto",Arial,sans-serif;color:var(--text)}
.stage{position:absolute;left:0;width:770px;background:var(--bg-green)}
.stage--home{top:0;height:558px}
.stage--account{top:620px;height:580px}
.page{position:absolute;left:75px;width:620px;background:var(--white)}
.stage--home .page{top:26px;height:489px}
.stage--account .page{top:27px;height:527px}

.topnav{position:absolute;left:194px;top:0;width:426px;height:27px;
  background:linear-gradient(180deg,var(--green) 0%,var(--green-light) 100%);
  display:flex;align-items:center;justify-content:center;gap:14px;font-size:9px;color:var(--white)}
.topnav span.sep{opacity:.9}
.brand{position:absolute;left:14px;top:14px;display:flex;align-items:center;gap:6px}
.brand__dot{width:40px;height:40px;border-radius:50%;background:var(--gold)}
.brand__name{font-size:28px;font-weight:700;color:var(--rust);line-height:1}
.brand__sub{font-size:28px;font-weight:700;color:var(--rust)}

.cta{position:absolute;top:41px;width:124px;height:44px;color:var(--white);padding:9px 0 0 17px;font-size:12px}
.cta small{display:block;font-size:7px;margin-top:2px}
.cta--quote{left:194px;background:var(--rust)}
.cta--raters{left:333px;background:var(--ochre)}
.cta--board{left:473px;background:var(--gold)}
.cta-rule{position:absolute;left:597px;top:78px;width:23px;height:7px;background:var(--yellow)}

.process{position:absolute;left:0;top:93px;width:620px;height:116px;background:var(--rust)}
.step{position:absolute;top:31px;width:79px;height:78px;border:2px solid var(--yellow);border-radius:6px;
  background:linear-gradient(180deg,var(--gold),var(--rust-dark));color:var(--white);
  font-family:"Oswald",Arial,sans-serif;font-weight:300;font-size:11px;line-height:1.15;padding:14px 0 0 5px;text-transform:uppercase}
.step b{display:block;font-weight:600;font-size:17px;line-height:1.1}
.step__icon{position:absolute;right:-7px;top:-18px;width:34px;height:34px;border-radius:50%;
  border:2px solid var(--yellow);background:var(--rust)}
.step__icon svg{width:100%;height:100%}
.arrow{position:absolute;top:58px;width:26px;height:38px}

.login{position:absolute;left:27px;top:226px;width:130px}
.heading{font-size:16px;color:var(--rust);font-weight:400}
.label{font-size:9px;color:var(--rust);margin-top:7px;text-transform:uppercase}
.field{height:12px;border:1px solid #bbb;margin-top:5px}
.links{font-size:9px;color:var(--rust);margin-top:16px;line-height:1.35}
.login-btn{margin:12px 0 0 58px;width:69px;height:23px;border-radius:12px;
  background:linear-gradient(90deg,var(--rust),var(--gold));color:var(--white);font-size:12px;
  display:flex;align-items:center;justify-content:center;gap:4px}
.dashed{border-top:1px dashed var(--rust);margin-top:11px}
.testimonial{font-size:8.5px;color:var(--rust);line-height:1.3;margin-top:6px}
.testimonial em{color:var(--gold)}
.intro{position:absolute;left:197px;top:223px;width:396px;font-size:6.8px;line-height:1.45;color:#555}
.intro p{margin-bottom:9px}
.intro .highlight{color:var(--green)}
.intro ul{list-style:none;margin-bottom:9px}
.intro li::before{content:"• "}

.help{position:absolute;left:567px;top:37px;text-align:center;font-size:11px;color:var(--rust)}
.help__circle{width:26px;height:26px;border-radius:50%;background:var(--rust);border:2px solid var(--gold);
  color:var(--white);font-weight:700;font-size:14px;display:flex;align-items:center;justify-content:center;margin:0 auto 2px}
.banner{position:absolute;left:0;top:86px;width:620px;height:35px;
  background:linear-gradient(90deg,var(--rust) 40%,var(--yellow) 100%);color:var(--white);font-size:24px;font-weight:300;padding:2px 0 0 27px}
.details-title{position:absolute;left:27px;top:128px;font-size:15px;font-weight:500;color:var(--rust)}
.details{position:absolute;left:27px;top:155px;display:flex}
.col{width:146px;padding-right:12px;margin-right:12px;border-right:1px solid var(--gold)}
.col:nth-child(2){width:152px}
.col:last-child{border-right:1px solid var(--gold)}
.item{font-size:8.5px;color:var(--rust);padding-bottom:4px;border-bottom:1px dashed var(--rust);margin-bottom:7px;line-height:1.5}
.edit{position:absolute;left:487px;top:205px;background:var(--rust);color:var(--white);font-size:8px;padding:1px 3px}
.tab{position:absolute;top:236px;width:124px;height:41px;color:var(--white);font-size:12px;padding:10px 0 0 17px}
.tab--quoting{left:26px;background:var(--green)}
.tab--active{left:166px;background:var(--rust)}
.tab--done{left:305px;background:var(--blue)}
.tab-rule{position:absolute;left:26px;top:277px;width:594px;height:4px;background:var(--green)}
.table-title{position:absolute;left:24px;top:295px;font-size:15px;font-weight:500;color:var(--green)}
table{position:absolute;left:26px;top:318px;width:581px;border-collapse:collapse;font-size:9px;color:#555}
th{background:var(--green);color:var(--white);font-weight:400;text-align:left;vertical-align:top;padding:6px 6px;height:39px;border-right:1px solid var(--white);line-height:1.2}
td{height:39px;vertical-align:top;padding:8px 6px;border-right:1px solid var(--white)}
tr:nth-child(odd) td{background:var(--row-a)}
tr:nth-child(even) td{background:var(--row-b)}
td.actions{padding:3px 2px;display:flex;justify-content:space-around}
.act{text-align:center;font-size:6px;color:var(--green)}
.act svg{width:21px;height:21px;display:block;margin:0 auto 1px}
</style>
</head>
<body>

<section class="stage stage--home">
  <div class="page">
    <nav class="topnav"><span>Home</span><span class="sep">|</span><span>How it works?</span><span class="sep">|</span><span>About Us</span><span class="sep">|</span><span>Testimonials</span><span class="sep">|</span><span>Contact Us</span></nav>
    <div class="brand"><span class="brand__dot"></span><span class="brand__name">Verdio</span></div>
    <div class="cta cta--quote">Get a quote</div>
    <div class="cta cta--raters">Energy Raters<small>Add your business</small></div>
    <div class="cta cta--board">Active Job Board</div>
    <div class="cta-rule"></div>

    <div class="process">
      <div class="step" style="left:35px"><b>Post</b>a job
        <span class="step__icon"><svg viewBox="0 0 34 34"><rect x="10" y="10" width="14" height="11" fill="none" stroke="#fff" stroke-width="1.6"/><path d="M13 24h8" stroke="#fff" stroke-width="1.6"/></svg></span></div>
      <svg class="arrow" style="left:119px" viewBox="0 0 26 38"><path d="M3 2l18 17-18 17" fill="none" stroke="#fff" stroke-width="5"/></svg>
      <div class="step" style="left:151px"><b>Get</b>as many quotes as you like
        <span class="step__icon"><svg viewBox="0 0 34 34"><rect x="11" y="9" width="10" height="14" fill="none" stroke="#fff" stroke-width="1.6" transform="rotate(15 16 16)"/></svg></span></div>
      <svg class="arrow" style="left:235px" viewBox="0 0 26 38"><path d="M3 2l18 17-18 17" fill="none" stroke="#fff" stroke-width="5"/></svg>
      <div class="step" style="left:267px"><b>Select</b>energy quote that suits
        <span class="step__icon"><svg viewBox="0 0 34 34"><path d="M15 9v10M15 14h6v8h-8l-3-4" fill="none" stroke="#fff" stroke-width="1.6"/></svg></span></div>
      <svg class="arrow" style="left:351px" viewBox="0 0 26 38"><path d="M3 2l18 17-18 17" fill="none" stroke="#fff" stroke-width="5"/></svg>
      <div class="step" style="left:384px"><b>Approve</b>payment
        <span class="step__icon"><svg viewBox="0 0 34 34"><path d="M10 17l5 5 9-10" fill="none" stroke="#fff" stroke-width="2.4"/></svg></span></div>
      <svg class="arrow" style="left:468px" viewBox="0 0 26 38"><path d="M3 2l18 17-18 17" fill="none" stroke="#fff" stroke-width="5"/></svg>
      <div class="step" style="left:500px"><b>Receive</b>rating
        <span class="step__icon"><svg viewBox="0 0 34 34"><g fill="none" stroke="#fff" stroke-width="1.2"><path d="M17 8l1.6 3.4 3.6.4-2.7 2.4.8 3.6-3.3-1.9-3.3 1.9.8-3.6-2.7-2.4 3.6-.4z"/><path d="M11 16l1.2 2.5 2.6.3-2 1.8.6 2.6-2.4-1.4-2.4 1.4.6-2.6-2-1.8 2.6-.3z"/><path d="M23 16l1.2 2.5 2.6.3-2 1.8.6 2.6-2.4-1.4-2.4 1.4.6-2.6-2-1.8 2.6-.3z"/></g></svg></span></div>
    </div>

    <aside class="login">
      <h2 class="heading">Login</h2>
      <div class="label">Email Address</div><div class="field"></div>
      <div class="label">Password</div><div class="field"></div>
      <div class="links">Forgot your password?<br>Register now</div>
      <div class="login-btn">Login <svg width="9" height="13" viewBox="0 0 9 13"><path d="M1 1l6 5.5L1 12" fill="none" stroke="#fff" stroke-width="2"/></svg></div>
      <div class="dashed"></div>
      <h2 class="heading" style="margin-top:12px">Testimonials</h2>
      <p class="testimonial">Lorem ipsum dolor sit amet, consectetur adipiscing elit. Praesent nisl nisi, consectetur a sollicitudin et, hendrerit eu. <em>Suscipit Bibendum.</em></p>
    </aside>

    <div class="intro">
      <p>verdio australia is Australia's leading professional energy rating consultancy firm specializing in large scaled residential and commercial energy rating logistics.</p>
      <p>We have professional and accredited energy raters in all States and Territories ready and waiting to provide quotes for and perform your energy rating jobs!</p>
      <p class="highlight">It's Free, Fast and Easy to use and you get the best price and turnaround time that suits you!!</p>
      <p>Register with us, upload your job and specifications, and sit back and watch as energy raters provide quotes for your work!</p>
      <ul>
        <li>Get the best priced quotes for your energy ratings</li>
        <li>Save time by listing a job to get many quotes</li>
        <li>Monitor your jobs and quotes on your own job board</li>
        <li>Be notified via email of all new quotes as they come in</li>
        <li>Be able to specify your desired turnaround times</li>
        <li>Accessible anytime and anywhere</li>
        <li>Choose a deadline for energy raters to supply quotes</li>
        <li>Have access to many qualified energy raters in your state all quoting for your work</li>
        <li>Be able to track your jobs and pay online</li>
        <li>Provide feedback on energy raters</li>
      </ul>
      <p>Its totally free to be registered with us and there is no obligations or hidden catches! So if you wish to utilise the amazing opportunity register now! This new website will be going live on the (insert date) so be ready to save some money!</p>
    </div>
  </div>
</section>

<section class="stage stage--account">
  <div class="page">
    <nav class="topnav"><span>Home</span><span class="sep">|</span><span>How it works?</span><span class="sep">|</span><span>About Us</span><span class="sep">|</span><span>Testimonials</span><span class="sep">|</span><span>Contact Us</span></nav>
    <div class="brand"><span class="brand__dot"></span><span class="brand__name">Verdio</span></div>
    <div class="help"><div class="help__circle">?</div>help</div>
    <div class="banner">My Account</div>
    <h2 class="details-title">Company Details</h2>
    <div class="details">
      <div class="col"><div class="item">CONTACT PERSON:<br>Sam Carter</div><div class="item">EMAIL ADDRESS:<br>scarter@mailbox.test</div></div>
      <div class="col"><div class="item">STREET ADDRESS:<br>Level 2, 118 Harbour Lane</div><div class="item">SUBURB<br>Elmwood</div></div>
      <div class="col"><div class="item">STATE<br>VIC</div><div class="item">POSTCODE<br>3100</div></div>
    </div>
    <div class="edit">EDIT</div>
    <div class="tab tab--quoting">Jobs for quoting</div>
    <div class="tab tab--active">Active Jobs</div>
    <div class="tab tab--done">Completed Jobs</div>
    <div class="tab-rule"></div>
    <h2 class="table-title">Jobs for Quoting</h2>
    <table>
      <colgroup><col style="width:77px"><col style="width:62px"><col style="width:54px"><col style="width:78px"><col style="width:78px"><col style="width:62px"><col style="width:77px"><col style="width:93px"></colgroup>
      <tr><th>Job</th><th>Quote No</th><th>Price</th><th>Total Price</th><th>Turnaround Time</th><th>Rework Price</th><th>Energy Raters Accreditation</th><th></th></tr>
      <tr><td>Lorem Ipsum</td><td>1111</td><td>$110.00</td><td>$180.65</td><td>1-5 days</td><td>$120.00</td><td>VIC</td><td class="actions">
        <span class="act"><svg viewBox="0 0 22 22"><circle cx="11" cy="11" r="10" fill="#5cb83a" stroke="#fff"/><path d="M6 11l4 4 6-8" fill="none" stroke="#fff" stroke-width="2.4"/></svg>Accept</span>
        <span class="act"><svg viewBox="0 0 22 22"><circle cx="11" cy="11" r="10" fill="#5cb83a" stroke="#fff"/><path d="M7 7l8 8M15 7l-8 8" stroke="#fff" stroke-width="2.4"/></svg>Decline</span>
        <span class="act"><svg viewBox="0 0 22 22"><circle cx="11" cy="11" r="10" fill="#5cb83a" stroke="#fff"/><rect x="6" y="7.5" width="10" height="7" fill="none" stroke="#fff" stroke-width="1.5"/><path d="M6 7.5l5 4 5-4" fill="none" stroke="#fff" stroke-width="1.5"/></svg>Email</span></td></tr>
      <tr><td>Lorem Ipsum</td><td>1111</td><td>$110.00</td><td>$180.65</td><td>1-5 days</td><td>$120.00</td><td>VIC</td><td class="actions">
        <span class="act"><svg viewBox="0 0 22 22"><circle cx="11" cy="11" r="10" fill="#5cb83a" stroke="#fff"/><path d="M6 11l4 4 6-8" fill="none" stroke="#fff" stroke-width="2.4"/></svg>Accept</span>
        <span class="act"><svg viewBox="0 0 22 22"><circle cx="11" cy="11" r="10" fill="#5cb83a" stroke="#fff"/><path d="M7 7l8 8M15 7l-8 8" stroke="#fff" stroke-width="2.4"/></svg>Decline</span>
        <span class="act"><svg viewBox="0 0 22 22"><circle cx="11" cy="11" r="10" fill="#5cb83a" stroke="#fff"/><rect x="6" y="7.5" width="10" height="7" fill="none" stroke="#fff" stroke-width="1.5"/><path d="M6 7.5l5 4 5-4" fill="none" stroke="#fff" stroke-width="1.5"/></svg>Email</span></td></tr>
      <tr><td>Lorem Ipsum</td><td>1111</td><td>$110.00</td><td>$180.65</td><td>1-5 days</td><td>$120.00</td><td>VIC</td><td class="actions">
        <span class="act"><svg viewBox="0 0 22 22"><circle cx="11" cy="11" r="10" fill="#5cb83a" stroke="#fff"/><path d="M6 11l4 4 6-8" fill="none" stroke="#fff" stroke-width="2.4"/></svg>Accept</span>
        <span class="act"><svg viewBox="0 0 22 22"><circle cx="11" cy="11" r="10" fill="#5cb83a" stroke="#fff"/><path d="M7 7l8 8M15 7l-8 8" stroke="#fff" stroke-width="2.4"/></svg>Decline</span>
        <span class="act"><svg viewBox="0 0 22 22"><circle cx="11" cy="11" r="10" fill="#5cb83a" stroke="#fff"/><rect x="6" y="7.5" width="10" height="7" fill="none" stroke="#fff" stroke-width="1.5"/><path d="M6 7.5l5 4 5-4" fill="none" stroke="#fff" stroke-width="1.5"/></svg>Email</span></td></tr>
      <tr><td>Lorem Ipsum</td><td>1111</td><td>$110.00</td><td>$180.65</td><td>1-5 days</td><td>$120.00</td><td>VIC</td><td class="actions">
        <span class="act"><svg viewBox="0 0 22 22"><circle cx="11" cy="11" r="10" fill="#5cb83a" stroke="#fff"/><path d="M6 11l4 4 6-8" fill="none" stroke="#fff" stroke-width="2.4"/></svg>Accept</span>
        <span class="act"><svg viewBox="0 0 22 22"><circle cx="11" cy="11" r="10" fill="#5cb83a" stroke="#fff"/><path d="M7 7l8 8M15 7l-8 8" stroke="#fff" stroke-width="2.4"/></svg>Decline</span>
        <span class="act"><svg viewBox="0 0 22 22"><circle cx="11" cy="11" r="10" fill="#5cb83a" stroke="#fff"/><rect x="6" y="7.5" width="10" height="7" fill="none" stroke="#fff" stroke-width="1.5"/><path d="M6 7.5l5 4 5-4" fill="none" stroke="#fff" stroke-width="1.5"/></svg>Email</span></td></tr>
    </table>
  </div>
</section>

</body>
</html>
```